'Shires at Roundtable'

We are after a flyer to sell a two day conference to sponsors, delegates and other Councils to participate.
The conference aims to be a forum for Northern Territory Councils to get together and discuss ideas, issues and overcome challenges and isolation in collaboration.
The conference will be a inaugural event with the plan to host a annual two day conference each year with a specific theme relevant to all Northern Territory Councils. - Give the Councils a voice.

```html
<!DOCTYPE html>
<html lang="en">
<head>
<meta charset="utf-8">
<title>Shires at Roundtable – Conference Flyer</title>
<link rel="stylesheet" href="https://fonts.googleapis.com/css2?family=Arimo:ital,wght@0,400;0,700;1,400;1,700&display=swap">
<style>
  :root {
    --page-bg: #f4f4f4;
    --steel-light: #e6e6e6;
    --steel-mid: #b4b4b4;
    --band-dark: #2e2e2e;
    --band-mid: #4a4a4a;
    --ink-white: #ffffff;
    --ink-dark: #2b2b2b;
    --ink-body: #1e1e1e;
    --sea-light: #4fb7c4;
    --sea-deep: #1f6f86;
    --sky: #c9d8e3;
    --hill-green: #4d6b35;
    --hill-dark: #2c3d22;
  }
  * { margin: 0; padding: 0; box-sizing: border-box; }
  html, body {
    width: 1200px; height: 523px; overflow: hidden;
    background: var(--page-bg);
    font-family: "Arimo", Arial, sans-serif;
  }
  .flyer {
    position: absolute; left: 420px; top: 11px;
    width: 360px; height: 500px; overflow: hidden;
    background: linear-gradient(180deg, var(--steel-mid) 0%, var(--steel-light) 22%, var(--steel-mid) 42%, var(--steel-light) 70%, var(--steel-mid) 100%);
    box-shadow: 0 4px 14px rgba(0,0,0,.25);
  }
  .photo { position: absolute; }
  .photo--coast {
    left: 170px; top: 0; width: 190px; height: 211px;
    background: linear-gradient(170deg, var(--sky) 0%, var(--sky) 15%, var(--sea-light) 40%, var(--sea-deep) 75%, var(--hill-green) 100%);
  }
  .photo--hills {
    left: 0; top: 280px; width: 178px; height: 220px;
    background: linear-gradient(180deg, var(--sky) 0%, var(--hill-green) 28%, var(--hill-dark) 100%);
  }
  .title {
    position: absolute; left: 14px; top: 22px;
    color: var(--ink-white); font-weight: 700; font-style: italic;
    text-transform: uppercase; line-height: .95;
    text-shadow: 0 1px 2px rgba(0,0,0,.25);
  }
  .title__main { display: block; font-size: 30px; }
  .title__sub { display: block; font-size: 16px; font-weight: 400; margin-top: 3px; }
  .title__rule {
    position: absolute; left: 14px; top: 106px; width: 150px; height: 1px;
    background: var(--ink-white);
  }
  .dates {
    position: absolute; left: 14px; top: 112px;
    color: var(--ink-dark); font-size: 27px; line-height: 1.05;
  }
  .dates span { display: block; }
  .dates__month { font-style: italic; }
  .band {
    position: absolute; left: 0; top: 211px; width: 360px; height: 69px;
    background: repeating-linear-gradient(180deg, var(--band-dark) 0 2px, var(--band-mid) 2px 4px);
  }
  .emblem { position: absolute; left: 92px; top: 168px; }
  .values {
    position: absolute; left: 188px; top: 360px; width: 164px;
    color: var(--ink-body); font-size: 5.6px; line-height: 1.2;
  }
  .values h3 { font-size: 6.2px; font-style: italic; font-weight: 400; text-transform: uppercase; margin-top: 1px; }
  .mission {
    position: absolute; left: 12px; top: 404px; width: 168px;
    color: var(--ink-white); font-style: italic; text-transform: uppercase;
  }
  .mission h2 { font-size: 12px; font-weight: 700; line-height: 1.1; }
  .mission p { font-size: 6px; font-weight: 700; line-height: 1.2; margin-bottom: 4px; }
</style>
</head>
<body>
  <main class="flyer">
    <div class="photo photo--coast" role="img" aria-label="Aerial photograph of a turquoise coastal bay and reef"></div>
    <div class="photo photo--hills" role="img" aria-label="Photograph of green coastal hills and ridgeline"></div>

    <h1 class="title">
      <span class="title__main">Shires</span>
      <span class="title__main">at</span>
      <span class="title__sub">Roundtable</span>
    </h1>
    <div class="title__rule"></div>
    <p class="dates"><span>13th-14th</span><span class="dates__month">April 2011</span></p>

    <div class="band"></div>
    <svg class="emblem" width="156" height="156" viewBox="0 0 156 156" role="img" aria-label="Round emblem with sweeping silver ribbon graphic">
      <defs>
        <radialGradient id="emblem-fill" cx=".6" cy=".4" r=".7">
          <stop offset="0" stop-color="#e8e8e8"/>
          <stop offset=".45" stop-color="#8a8a8a"/>
          <stop offset="1" stop-color="#2a2a2a"/>
        </radialGradient>
      </defs>
      <circle cx="78" cy="78" r="75" fill="url(#emblem-fill)" stroke="#ffffff" stroke-width="2"/>
    </svg>

    <section class="values">
      <h3>Core Values</h3>
      <p>We have identified these key values and principles as integral to the achievement of our vision.</p>
      <h3>Respect</h3>
      <p>Acknowledge and value individual community identity indigenous culture and heritage, in an environment free of discrimination.</p>
      <h3>Professionalism</h3>
      <p>Administration, planning, logistics, communications and governance of the highest standard.</p>
      <h3>Results</h3>
      <p>Achievement of agreed service delivery standards.</p>
      <h3>Integrity</h3>
      <p>Dealing honestly and fairly with all stakeholders.</p>
      <h3>Innovation</h3>
      <p>Developing new ways of delivering services and solving implementation problems.</p>
      <h3>Engagement</h3>
      <p>Listen effectively to residents and ratepayers and collaborate with Stakeholders.</p>
    </section>

    <section class="mission">
      <h2>Vision &amp; Mission</h2>
      <p>A region whose people are healthy, happy and positive about their future.</p>
      <h2>Objective</h2>
      <p>A strong, reliable and responsible shire council that will support the people of Coral Coast by providing a range of high quality services that lead to community, cultural, economic and environmental wellbeing.</p>
    </section>
  </main>
</body>
</html>
```